Packaging and labelling for Swiss made Organic CBD Oil

Visit our website www.velmarotiva.com
We have not put any product on yet as require packaging and label design .
Website will give you a great feel for the company and how we have used
the logo . The Drevask cbd product shown is a company similar to ourselves with similar core values , we liked the clean packaging design they have .

Im happy if you want use the mandala symbol in our logo separate from
VELMARO, to separate and use the mandala symbol as a larger icon than
it appears in our logo
Clean , Pure , organic feel. Like the product to look pharmaceutical and life changing not gimmicky.
Colours to go with or be the same as our logo colours
But not too cold and clinical
Bottle size 84mm x 25mm
Label size 75mm x 30mm
Box 30mm x 30mm x 100mm
6 products
Full Spectrum :
500mg CBD (5%)
1000mg CBD ( 10% )
1500mg CBD (15%)
2000mg CBD ( 20% )
Broad spectrum THC Free
500mg CBD (5%)
Pets
500mg Broad Spectrum THC Free
Updates

Would like the design to be more modern than traditional

LABEL Information Front of Bottle - Logo VELMARO & Mandala - Mandala can be used separately as design symbol Organic Cannabis Oil 1500mg CBD (15%) Ful Spectrum 10ml Back of bottle Ingredients: Organic Cannabis Oil Extract Organic Sunflower Seed Oil THC - 0.2% Certified Swiss Organic Cultivation Shake well before use. Store in a cool , dry place and out of the each of children BOX information Front and rear Logo - VELMARO & Mandala - Mandala can be used separately as a design symbol Organic Cannabis Oil 1500mg CBD (15%) Full Spectrum Sides x 2 This product is a food supplement and is not intended to diagnose, treat, cure or prevent any disease If you are pregnant, lactating or taking any medication consult your health care practitioner Suitable for vegetarians and vegans Ingredients Organic Cannabis Oil extract Organis Sunflower Oil Store in a cool ,dry place, out of the reach of children Recommended Use 1-5 drops ( 1 drop = 7.5mg CBD ) Subject to body weight and personal requirement - visit www.velmarotiva for more information 100% Natural 100% Organic GMO free 100% Vegan ( symbol with each ) Expiry date see bottle label Cultivated and manufactured in Switzerland

Target Market(s)

age 40 - 80

Font styles to use
Other font styles liked:
• In our website we have used Open Sans for the copy and Lato for headings .

Requirements
Must have
• look like an Industry leader
Velmaro will change the quality of peoples lives and in some cases may
even save lives so want look powerful and credible
Our Mission is - Through Delivering Pure , Premium , Organic products we will educate, inform and help people achieve healthier , happier lifestyles
Nice to have
• Colours to look good with our logo colours or be the same as our logo
colours
Logo Font - Avenir Black and Avenir Book

Font used in website - Content - Open Sans / Headings - Lato
If you have another font for the packaging information that will go well with
our logo, I'm happy for you to use your skills

```html
<!DOCTYPE html>
<html lang="en">
<head>
<meta charset="utf-8">
<title>Velmaro Full Spectrum CBD Oil – Packaging</title>
<link rel="stylesheet" href="https://fonts.googleapis.com/css2?family=EB+Garamond:wght@400;500;600&display=swap">
<style>
  :root {
    --backdrop: #e3e4e6;
    --teal: #0b4a50;
    --teal-side: #083e43;
    --teal-label: #0e545a;
    --mint: #9edbd5;
    --ink-light: #f2f6f6;
    --panel-rule: #cfe3e1;
  }
  * { box-sizing: border-box; margin: 0; padding: 0; }
  html, body { width: 1200px; height: 1200px; overflow: hidden; }
  body {
    background: var(--backdrop);
    font-family: "EB Garamond", Georgia, serif;
    color: var(--ink-light);
    position: relative;
  }
  .box-flat { position: absolute; left: 150px; top: 150px; display: flex; }
  .panel { width: 250px; height: 950px; position: relative; }
  .panel--side { background: var(--teal-side); }
  .panel--front { background: var(--teal); }

  .mark-circle {
    position: absolute; left: 50%; transform: translateX(-50%);
    border-radius: 50%; border: 3px solid var(--mint);
  }
  .panel--side .mark-circle { width: 120px; height: 120px; top: 155px; }
  .panel--front .mark-circle { width: 180px; height: 180px; top: 125px; }

  .notice {
    position: absolute; left: 27px; width: 196px;
    border: 1px solid var(--panel-rule);
    padding: 0 0 8px; font-size: 12.5px; line-height: 1.45;
  }
  .notice--storage { top: 460px; }
  .notice--warning { top: 585px; }
  .notice__title {
    display: inline-block; background: var(--ink-light); color: var(--teal-side);
    font-size: 10px; letter-spacing: .04em; padding: 1px 6px; margin-bottom: 6px;
    text-transform: uppercase;
  }
  .notice__body { padding: 0 8px; }

  .product-title {
    position: absolute; left: 0; right: 0; top: 470px;
    text-align: center; line-height: 1; font-weight: 600;
  }
  .product-title__kicker { display: block; font-size: 25px; font-weight: 500; }
  .product-title__main { display: block; font-size: 46px; margin-top: 8px; }

  .spec-frame {
    position: absolute; left: 50%; transform: translateX(-50%);
    width: 176px; border: 2px solid var(--panel-rule);
    text-align: center; padding: 14px 0 12px;
  }
  .panel--front .spec-frame { top: 640px; }
  .spec-frame__top, .spec-frame__bottom {
    position: absolute; left: 50%; transform: translateX(-50%);
    background: var(--teal); padding: 0 5px; white-space: nowrap; line-height: 1.2;
  }
  .spec-frame__top { top: -14px; font-size: 21px; }
  .spec-frame__bottom { bottom: -12px; font-size: 18px; }
  .spec-frame__dose { font-size: 25px; font-weight: 600; line-height: 1.2; }

  .origin {
    position: absolute; left: 0; right: 0; text-align: center;
    font-size: 19px; font-weight: 600;
  }
  .panel--front .origin { top: 870px; }

  .label-flat {
    position: absolute; left: 760px; top: 430px; width: 290px; height: 400px;
    background: var(--teal-label);
  }
  .label-flat .mark-circle { width: 120px; height: 120px; top: 40px; }
  .brand-name {
    position: absolute; left: 0; right: 0; top: 180px; text-align: center;
    font-size: 32px; font-weight: 600; letter-spacing: .12em;
  }
  .label-flat .spec-frame { top: 270px; width: 186px; padding: 12px 0 10px; }
  .label-flat .spec-frame__top, .label-flat .spec-frame__bottom { background: var(--teal-label); }
  .label-flat .spec-frame__top { font-size: 20px; }
  .label-flat .spec-frame__dose { font-size: 24px; }
  .label-flat .origin { top: 352px; font-size: 18px; }
</style>
</head>
<body>
  <section class="box-flat" aria-label="Carton, side and front panels">
    <div class="panel panel--side">
      <div class="mark-circle"></div>
      <div class="notice notice--storage">
        <span class="notice__title">Do not refrigerate</span>
        <p class="notice__body">Keep at room temperature to preserve freshness. Store away from humidity, heat, and light.</p>
      </div>
      <div class="notice notice--warning">
        <span class="notice__title">FDA warning statement</span>
        <p class="notice__body">If pregnant, nursing or taking prescription drugs, consult your physician prior to use. Keep out of reach of children.</p>
      </div>
    </div>
    <div class="panel panel--front">
      <div class="mark-circle"></div>
      <h1 class="product-title">
        <span class="product-title__kicker">FULL SPECTRUM</span>
        <span class="product-title__main">CBD OIL</span>
      </h1>
      <div class="spec-frame">
        <span class="spec-frame__top">Organic CBD</span>
        <div class="spec-frame__dose">2000mg (20%)</div>
        <span class="spec-frame__bottom">THC Free</span>
      </div>
      <p class="origin">Made in Swiss</p>
    </div>
  </section>

  <section class="label-flat" aria-label="Bottle label">
    <div class="mark-circle"></div>
    <p class="brand-name">VELMARO</p>
    <div class="spec-frame">
      <span class="spec-frame__top">Organic CBD</span>
      <div class="spec-frame__dose">2000mg (20%)</div>
      <span class="spec-frame__bottom">THC Free</span>
    </div>
    <p class="origin">Made in Swiss</p>
  </section>
</body>
</html>
```